Core Values poster for display in office

We want to create a poster that displays our core values which we can print and place in our office and potentially use on our website.

DataHaven is a Cyber Security consultancy that helps its secure its clients from Cyber Criminals.

Our core values are what we live and breath everyday. They are:
- Customer love
- High performing team
- Do the right thing
- An awesome culture
- Innovative

Here they are again with more detail after each:
- Customer love – exchange in abundance
- High performing team – do whatever it takes, no passengers
- Do the right thing – be accountable, maintain our integrity
- An awesome culture – work hard, play hard, collaborate and celebrate success
- Innovative – solving problems with new ideas

We are in the process of rolling out new branding with a load of comic book style super hero's and villains. Attached are some of those images in PDF format for some business card designs for you to review if you want to incorporate, but I will upload these images to this dropbox folder once my designer sends them to me:
https://www.filecrate.example/sh/qpwlzrtkc42hsum/KKTm7VoP2wQ8yE5nLDRxUa91b?dl=0

I stumbled across another business with the same name as us and saw their values poster, which I liked conceptually.
www.datahaven.example
I've attached the image for reference (note this is not our business or values - just saying I like the concept).

Also attached is our logo in EPS format.

We would like the image editing version of the file once complete so we can edit the file in case we change or tweak our values in the near future.

Target Market(s)

This poster is to be displayed internally and maybe on our website in the hiring section

Industry/Entity Type

Office

Colors
0792cd
ffffff
f68e4e
e667a6
fbee3e

Requirements
Must have
• Must have a vibrant, impactful poster that clearly states our core values in a way so that they are understood.
• Must be print ready in high definition (large A2 size poster).
Nice to have
• Integrate our logo

```html
<!DOCTYPE html>
<html lang="en">
<head>
<meta charset="utf-8">
<title>DataHaven Core Values Poster</title>
<link rel="stylesheet" href="https://fonts.googleapis.com/css2?family=Bangers&family=Nunito:wght@700&display=swap">
<style>
  :root {
    --brand-blue: #0792cd;
    --white: #ffffff;
    --orange: #f68e4e;
    --pink: #e667a6;
    --yellow: #fbee3e;
    --ink: #111111;
    --logo-grey: #6d6e71;
    --title-box: #cfe9f5;
  }
  * { box-sizing: border-box; margin: 0; padding: 0; }
  html, body { width: 849px; height: 1200px; overflow: hidden; background: var(--white); }
  .poster {
    position: relative; width: 849px; height: 1200px;
    background: var(--brand-blue); overflow: hidden;
    font-family: "Bangers", "Impact", sans-serif;
  }
  .poster__frame {
    position: absolute; left: 22px; top: 22px; right: 22px; bottom: 22px;
    border: 3px solid var(--pink);
  }
  .poster__panel {
    position: absolute; left: 51px; top: 57px; width: 747px; height: 1103px;
    background: var(--yellow); border: 4px solid var(--ink);
  }
  .poster__shapes { position: absolute; left: 0; top: 0; width: 849px; height: 1200px; }
  .burst-outer { fill: var(--orange); stroke: var(--ink); stroke-width: 4; stroke-linejoin: round; }
  .burst-inner { fill: var(--white); }
  .bubble-shape { fill: var(--white); stroke: var(--ink); stroke-width: 5; stroke-linejoin: round; }

  .brand {
    position: absolute; left: 0; right: 0; top: 96px;
    display: flex; align-items: center; justify-content: center; gap: 14px;
  }
  .brand__mark { width: 40px; height: 40px; border-radius: 50%; background: var(--brand-blue); }
  .brand__name {
    font-family: "Nunito", "Arial", sans-serif; font-weight: 700;
    font-size: 54px; color: var(--logo-grey); letter-spacing: 0.5px;
  }

  .value {
    position: absolute; transform: translate(-50%, -50%);
    display: flex; flex-direction: column; align-items: center; text-align: center;
    font-size: 28px; line-height: 1.04; letter-spacing: 1px;
  }
  .value__title { color: var(--ink); }
  .value__detail--orange { color: var(--orange); }
  .value__detail--pink { color: var(--pink); }
  .value--customer { left: 250px; top: 386px; width: 280px; }
  .value--team { left: 580px; top: 472px; width: 320px; }
  .value--right { left: 268px; top: 642px; width: 220px; font-size: 26px; }
  .value--culture { left: 615px; top: 783px; width: 300px; font-size: 26px; }
  .value--innovative { left: 268px; top: 972px; width: 300px; }

  .poster__title {
    position: absolute; left: 360px; top: 1044px; width: 420px; height: 80px;
    background: var(--title-box); display: flex; align-items: center; justify-content: center;
  }
  .poster__title h1 {
    font-weight: 400; font-size: 70px; color: var(--brand-blue);
    letter-spacing: 2px; -webkit-text-stroke: 2.5px var(--ink);
  }
</style>
</head>
<body>
<main class="poster">
  <div class="poster__frame"></div>
  <div class="poster__panel" role="img" aria-label="Yellow comic halftone dot background"></div>

  <svg class="poster__shapes" viewBox="0 0 849 1200" aria-hidden="true">
    <polygon class="burst-outer"
      points="110,8 210,55 270,5 340,50 425,3 510,50 580,5 640,55 740,8 715,120 770,175 690,200 715,290 590,245 510,295 425,250 340,295 260,245 135,290 160,200 80,175 135,120"/>
    <polygon class="burst-inner"
      points="160,55 240,85 285,48 350,85 425,48 500,85 565,48 610,85 690,55 670,135 710,170 645,188 660,250 580,218 505,258 425,222 345,258 270,218 190,250 205,188 140,170 180,135"/>

    <path class="bubble-shape" d="M398,385 A150,68 0 0 1 240,452 L170,510 L185,446 A150,68 0 1 1 398,385 Z"/>

    <ellipse class="bubble-shape" cx="580" cy="470" rx="172" ry="82"/>
    <circle class="bubble-shape" cx="695" cy="590" r="18"/>
    <circle class="bubble-shape" cx="722" cy="635" r="11"/>

    <polygon class="bubble-shape"
      points="95,510 175,555 255,515 300,560 410,520 385,590 460,615 390,660 435,730 345,715 300,780 250,735 155,760 160,700 80,670 140,630 90,575 160,585"/>

    <path class="bubble-shape" d="M793,785 A178,108 0 0 1 520,876 L475,930 L480,855 A178,108 0 1 1 793,785 Z"/>

    <path class="bubble-shape" d="M90,970 A180,78 0 0 1 350,900 L425,860 L395,914 A180,78 0 1 1 90,970 Z"/>
  </svg>

  <header class="brand">
    <span class="brand__mark"></span>
    <span class="brand__name">DataHaven</span>
  </header>

  <section class="value value--customer">
    <span class="value__title">Customer Love</span>
    <span class="value__detail value__detail--orange">Exchange in<br>Abundance</span>
  </section>

  <section class="value value--team">
    <span class="value__title">High Performing Team</span>
    <span class="value__detail value__detail--orange">Do Whatever<br>It Takes,<br>No Passengers</span>
  </section>

  <section class="value value--right">
    <span class="value__title">Do the Right<br>Thing</span>
    <span class="value__detail value__detail--pink">Be Accountable,<br>Maintain Our<br>Integrity</span>
  </section>

  <section class="value value--culture">
    <span class="value__title">An Awesome<br>Culture</span>
    <span class="value__detail value__detail--orange">Work Hard, Play<br>Hard, Collaborate<br>and Celebrate<br>Success</span>
  </section>

  <section class="value value--innovative">
    <span class="value__title">Innovative</span>
    <span class="value__detail value__detail--orange">Solving<br>Problems With<br>New Ideas</span>
  </section>

  <div class="poster__title"><h1>Core Values</h1></div>
</main>
</body>
</html>
```